Aviation Banner Ad Designs

SkyLedgerMetrics provides access to the most accurate aircraft operating cost information, to compare Piston, Turboprop and Jet aircraft.

The banners ads will be used for retargeting/remarketing - to bring visitors back to the site. The banners should remind and reinforce the key messages of what the site provides.

Target Market(s)

Private aircraft buyers including:
- Aircraft Brokers
- Charter Operators
- Corporate Flight Departments
- Aircraft Management companies
- Financial Institutions
- Aircraft Owners
- Prospective Buyers

Requirements
Must have
• A. Banner Objective
The visual and textual content of the banner should remind the viewer about the features of the site, and prompt them to return to the site.
1. Arresting visual
2. Headline
3. Single message
4. Compelling CTA
5. Logo - big enough to see
6. Standard DWR ad sizes/specs

B. Design Elements
Logo: As attached
Main Title: Calculate Jet Operating Costs
Subtitle: Compare Ownership Usage Scenarios
Call to Action Button: Compare Ownership Costs
Background: Several images supplied as options

C. Banner Sizes
Do examples as 300×250 , 728×90 , 160×600
Final sizes to also include 320×100 , 336x280 , 300x600

Finally delivery as .jpg files.

Font - use same font as on site

```html
<!DOCTYPE html>
<html lang="en">
<head>
<meta charset="utf-8">
<title>SkyLedgerMetrics Banner Set</title>
<link href="https://fonts.googleapis.com/css2?family=Bebas+Neue&display=swap" rel="stylesheet">
<style>
  :root {
    --canvas: #fdfdfd;
    --blue-light: #2bb0e4;
    --blue-mid: #1f8fd0;
    --blue-deep: #2a6ab8;
    --navy: #0d3a63;
    --ink: #1b2433;
    --white: #ffffff;
    --photo-sky: #b9c6cc;
    --photo-body: #d9cfa8;
    --photo-shade: #6d7b80;
    --logo-red: #d63a2f;
  }
  * { margin: 0; padding: 0; box-sizing: border-box; }
  html, body { width: 1200px; height: 1200px; overflow: hidden; background: var(--canvas); }
  body { position: relative; font-family: "Bebas Neue", "Arial Narrow", sans-serif; color: var(--white); }

  .banner { position: absolute; overflow: hidden; background: linear-gradient(180deg, var(--blue-light), var(--blue-mid)); }
  .banner svg.art { position: absolute; inset: 0; width: 100%; height: 100%; }

  .brand { position: absolute; display: flex; align-items: center; gap: 5px; color: var(--ink); letter-spacing: 0.04em; white-space: nowrap; }
  .brand-mark { background: var(--logo-red); flex: none; }

  .headline, .subline, .cta { position: absolute; text-transform: uppercase; }
  .cta { background: var(--navy); border-radius: 3px; display: flex; align-items: center; justify-content: center; gap: 8px; }
  .cta svg { flex: none; }

  /* 160x600 skyscraper */
  .sky { left: 212px; top: 222px; width: 134px; height: 756px; }
  .sky .brand { left: 16px; top: 14px; font-size: 14px; }
  .sky .brand-mark { width: 10px; height: 10px; }
  .sky .headline { left: 0; right: 0; top: 418px; text-align: center; font-size: 34px; line-height: 38px; }
  .sky .subline { left: 0; right: 0; top: 576px; text-align: center; font-size: 14px; line-height: 19px; }
  .sky .cta { left: 10px; top: 667px; width: 116px; height: 66px; border-radius: 5px; justify-content: flex-start; padding-left: 14px; gap: 6px; }
  .sky .cta span { font-size: 16px; line-height: 16px; }

  /* 728x90 leaderboard */
  .leader { left: 377px; top: 222px; width: 612px; height: 76px; border: 1px solid #d9e6ee; }
  .leader .brand { right: 12px; top: 29px; font-size: 15px; }
  .leader .brand-mark { width: 10px; height: 10px; }
  .leader .headline { left: 11px; top: 10px; font-size: 21px; line-height: 22px; }
  .leader .subline { left: 11px; top: 33px; font-size: 9.5px; line-height: 10px; }
  .leader .cta { left: 12px; top: 50px; width: 155px; height: 18px; font-size: 12px; }

  /* 300x250 medium rectangle */
  .rect { left: 374px; top: 322px; width: 253px; height: 211px; }
  .rect .brand { right: 8px; top: 18px; font-size: 9.5px; gap: 4px; letter-spacing: 0.02em; }
  .rect .brand-mark { width: 6px; height: 6px; }
  .rect .headline { left: 10px; top: 8px; font-size: 19px; line-height: 20px; }
  .rect .subline { left: 10px; top: 67px; font-size: 8.5px; line-height: 10px; }
  .rect .cta { left: 41px; top: 180px; width: 172px; height: 19px; font-size: 13px; }
</style>
</head>
<body>

  <section class="banner sky" aria-label="160 by 600 banner">
    <svg class="art" viewBox="0 0 134 756" preserveAspectRatio="none">
      <defs>
        <linearGradient id="skyPhoto" x1="0" y1="0" x2="1" y2="1">
          <stop offset="0" stop-color="var(--photo-sky)"/>
          <stop offset="0.5" stop-color="var(--photo-body)"/>
          <stop offset="1" stop-color="var(--photo-shade)"/>
        </linearGradient>
      </defs>
      <rect x="0" y="0" width="134" height="46" fill="var(--white)"/>
      <polygon role="img" aria-label="Business jet engine and fuselage on the ramp" points="134,46 0,147 0,400 134,290" fill="url(#skyPhoto)"/>
    </svg>
    <div class="brand"><span class="brand-mark"></span>SkyLedgerMetrics</div>
    <h1 class="headline">Calculate<br>Jet<br>Operating<br>Costs</h1>
    <p class="subline">Compare<br>ownership usage<br>scenarios</p>
    <a class="cta"><span>Compare<br>ownership<br>costs</span>
      <svg width="30" height="46" viewBox="0 0 30 46"><polyline points="6,3 26,23 6,43" fill="none" stroke="var(--white)" stroke-width="4"/></svg>
    </a>
  </section>

  <section class="banner leader" aria-label="728 by 90 banner">
    <svg class="art" viewBox="0 0 612 76" preserveAspectRatio="none">
      <defs>
        <linearGradient id="leaderPhoto" x1="0" y1="0" x2="1" y2="0">
          <stop offset="0" stop-color="var(--photo-sky)"/>
          <stop offset="0.5" stop-color="var(--photo-body)"/>
          <stop offset="1" stop-color="var(--photo-shade)"/>
        </linearGradient>
      </defs>
      <polygon role="img" aria-label="Business jet engine and fuselage on the ramp" points="228,0 433,0 496,76 290,76" fill="url(#leaderPhoto)"/>
      <polygon points="433,0 612,0 612,76 496,76" fill="var(--white)"/>
    </svg>
    <h1 class="headline">Calculate jet operating costs</h1>
    <p class="subline">Compare ownership usage scenarios</p>
    <a class="cta">Compare ownership costs
      <svg width="7" height="11" viewBox="0 0 7 11"><polyline points="1,1 6,5.5 1,10" fill="none" stroke="var(--white)" stroke-width="1.5"/></svg>
    </a>
    <div class="brand"><span class="brand-mark"></span>SkyLedgerMetrics</div>
  </section>

  <section class="banner rect" aria-label="300 by 250 banner">
    <svg class="art" viewBox="0 0 253 211" preserveAspectRatio="none">
      <defs>
        <linearGradient id="rectPhoto" x1="0" y1="1" x2="1" y2="0">
          <stop offset="0" stop-color="var(--photo-shade)"/>
          <stop offset="0.45" stop-color="var(--photo-body)"/>
          <stop offset="1" stop-color="var(--photo-sky)"/>
        </linearGradient>
      </defs>
      <polygon points="143,0 177,47 110,47" fill="var(--blue-deep)"/>
      <polygon points="143,0 253,0 253,47 177,47" fill="var(--white)"/>
      <polygon role="img" aria-label="Business jet with open cabin door on the ramp" points="10,211 177,47 253,47 253,125 180,211" fill="url(#rectPhoto)" opacity="0.92"/>
    </svg>
    <h1 class="headline">Calculate<br>jet operating<br>costs</h1>
    <p class="subline">Compare ownership<br>usage scenarios</p>
    <div class="brand"><span class="brand-mark"></span>SkyLedgerMetrics</div>
    <a class="cta">Compare ownership costs
      <svg width="7" height="11" viewBox="0 0 7 11"><polyline points="1,1 6,5.5 1,10" fill="none" stroke="var(--white)" stroke-width="1.5"/></svg>
    </a>
  </section>

</body>
</html>
```